Lady Marisol's Reserve Aged Bramblewick Rum LABEL

Tallpine Hollow Distillery is looking for a label for our new product (Lady Marisol's Reserve). This will be a barrel aged Rum that is distilled, bottled, and aged in small batches in Belmont, NC just outside of Charlotte, North Carolina. In the attached file (drink recipes) you will see the Product that we currently sell (Bramblewick Rum). The new product does not have to be the same style, but we would like to maintain some brand relevance. There are some other attachments to give you an idea about the look of the company. Also attached is a picture of the dark rum in the bottle. This is what the label will go onto.

-The label will most likely be printed on craft paper stock.

Industry/Entity Type

It Company

Requirements
Must have
• We need the following in the new label
-Company Name= Tallpine Hollow Distillery
-Product name= Lady Marisol's Reserve
-Product sub-name= Aged Bramblewick Rum
-Product description= Distilled Bottled and Aged by Tallpine Hollow Distillery
Nice to have
• We would like to incorporate a rendering of Lady Marisol or just a crown. We think this is important because Charlotte, NC is named after her.

```html
<!DOCTYPE html>
<html lang="en">
<head>
<meta charset="utf-8">
<title>Lady Marisol's Reserve – Aged Bramblewick Rum Label</title>
<link rel="stylesheet" href="https://fonts.googleapis.com/css2?family=Sorts+Mill+Goudy&display=swap">
<style>
  :root {
    --page: #ffffff;
    --kraft: #d3b387;
    --kraft-light: #e4cba0;
    --slate: #8d938f;
    --slate-dark: #7c837f;
    --ink: #1c1510;
    --title: #4a0d0e;
    --frame: #4b4740;
    --portrait: #cfc9c0;
    --portrait-dark: #8a847a;
  }
  * { margin: 0; padding: 0; box-sizing: border-box; }
  html, body {
    width: 1200px;
    height: 978px;
    overflow: hidden;
    background: var(--page);
  }
  .canvas {
    position: relative;
    width: 1200px;
    height: 978px;
  }
  .label {
    position: absolute;
    left: 307px;
    top: 49px;
    width: 586px;
    height: 880px;
    border: 6px solid var(--kraft-light);
    overflow: hidden;
    font-family: "Sorts Mill Goudy", "Goudy Old Style", Georgia, serif;
    color: var(--ink);
    text-align: center;
  }
  .label-texture {
    position: absolute;
    inset: 0;
    background:
      radial-gradient(ellipse 60% 30% at 20% 20%, var(--kraft) 0%, transparent 70%),
      radial-gradient(ellipse 50% 35% at 85% 45%, var(--kraft) 0%, transparent 70%),
      radial-gradient(ellipse 55% 30% at 25% 75%, var(--kraft) 0%, transparent 70%),
      radial-gradient(ellipse 45% 25% at 80% 92%, var(--kraft) 0%, transparent 70%),
      linear-gradient(160deg, var(--slate) 0%, var(--slate-dark) 100%);
  }
  .line {
    position: absolute;
    left: 0;
    width: 100%;
    line-height: 1;
  }
  .company {
    top: 24px;
    font-size: 25px;
  }
  .portrait {
    position: absolute;
    left: 130px;
    top: 51px;
    width: 306px;
    height: 460px;
  }
  .product-name {
    top: 450px;
    font-size: 60px;
    color: var(--title);
    line-height: 80px;
  }
  .sub-name {
    top: 662px;
    font-size: 36px;
    letter-spacing: 0.5px;
  }
  .abv {
    top: 734px;
    font-size: 16px;
  }
  .description {
    top: 792px;
    font-size: 25px;
    line-height: 35px;
  }
</style>
</head>
<body>
<main class="canvas">
  <section class="label">
    <div class="label-texture" role="img" aria-label="Mottled kraft paper and slate grey background pattern"></div>

    <p class="line company">Tallpine Hollow Distillery</p>

    <svg class="portrait" viewBox="0 0 306 460" aria-hidden="false">
      <defs>
        <radialGradient id="portrait-tone" cx="50%" cy="45%" r="60%">
          <stop offset="0%" stop-color="var(--portrait)"/>
          <stop offset="100%" stop-color="var(--portrait-dark)"/>
        </radialGradient>
      </defs>
      <ellipse cx="153" cy="230" rx="150" ry="226" fill="none" stroke="var(--frame)" stroke-width="6"/>
      <ellipse cx="153" cy="230" rx="140" ry="215" fill="url(#portrait-tone)" role="img" aria-label="Engraved portrait of Lady Marisol wearing a jewelled headdress, earrings and pearl necklace"/>
      <ellipse cx="153" cy="230" rx="140" ry="215" fill="none" stroke="var(--frame)" stroke-width="2"/>
    </svg>

    <h1 class="line product-name">Lady Marisol's<br>Reserve</h1>

    <p class="line sub-name">AGED BRAMBLEWICK RUM</p>

    <p class="line abv">40% ALC. BY VOL. (80 PROOF)</p>

    <p class="line description">Distilled Bottled and Aged by<br>Tallpine Hollow Distillery</p>
  </section>
</main>
</body>
</html>
```